GLNSTC - Website Design

We require a WordPress website for an accounting firm.
Please review our concept design found on our development site:
http://mossyquarry.ca/glnstuw.
The client would like to carry the look and feel of the National Corporate site http://www.gln.ca as well.
The site must be mobile ready (responsive)
The client will be providing a collection of staff photos for a contact page
Accounting

```html
<!DOCTYPE html>
<html lang="en">
<head>
<meta charset="utf-8">
<title>GLN Marlow Trent &amp; Associates</title>
<link rel="stylesheet" href="https://fonts.googleapis.com/css2?family=Cinzel:wght@400&family=Open+Sans:ital,wght@0,400;0,600;0,700;1,400&display=swap">
<style>
:root{
  --ink:#222;
  --text:#555;
  --muted:#999;
  --rule:#dcdcdc;
  --white:#fff;
  --side:#f1f1f1;
  --olive:#6b6a2a;
  --bookings:#8c2a30;
  --services:#9c3f1c;
  --events:#3a7473;
  --red:#b8272e;
  --teal:#4b7b80;
  --today:#a9ae7c;
  --footer:#151515;
  --footer-text:#8a8a8a;
}
*{box-sizing:border-box;margin:0;padding:0}
html,body{width:1200px;height:2452px;overflow:hidden}
body{position:relative;font-family:"Open Sans",Arial,sans-serif;color:var(--text);
  background:linear-gradient(180deg,#3a3028 0%,#2b2520 15%,#1c1a18 35%,#0d0d0d 60%,#080808 100%)}
.hero-scene{position:absolute;left:0;top:0;width:1200px;height:2109px;
  background:linear-gradient(180deg,#5a4a3e 0%,#6e4e34 12%,#4b3a2e 22%,#2e2924 34%,#1e1c1a 55%,#0b0b0b 100%)}
.abs{position:absolute}
/* header */
.site-header{left:100px;top:0;width:1000px;height:88px;background:var(--white);display:flex;align-items:center;justify-content:space-between;padding:0 38px 0 18px}
.brand{display:flex;align-items:center;gap:12px}
.brand-mark{width:36px;height:36px;background:var(--olive)}
.brand-name{font-family:"Cinzel",Georgia,serif;font-size:21px;color:#2a2a2a;line-height:1}
.brand-tag{font-family:"Cinzel",Georgia,serif;font-size:11px;color:#2a2a2a;margin-top:6px;border-top:2px solid var(--olive);padding-top:3px;letter-spacing:.5px}
.main-nav{display:flex;gap:66px;font-size:13px;color:#333}
/* hero */
.hero-sub{left:0;top:228px;width:1200px;text-align:center;font-family:"Cinzel",Georgia,serif;font-size:24px;color:#f3ece2;letter-spacing:1px}
.hero-title{left:0;top:262px;width:1200px;text-align:center;font-family:"Cinzel",Georgia,serif;font-size:37px;color:#fff;letter-spacing:1.5px}
.slider-arrow{left:48px;top:249px;width:34px;height:34px;border-radius:50%;background:rgba(255,255,255,.2)}
.slider-dot{left:117px;top:293px;width:7px;height:7px;border-radius:50%;background:rgba(255,255,255,.35)}
/* feature boxes */
.features{left:100px;top:471px;width:1000px;height:144px;display:flex}
.feature{flex:1;display:flex;padding:18px 20px 0 28px;gap:28px;color:#fff}
.feature+.feature{border-left:1px solid rgba(0,0,0,.25)}
.feature.bookings{background:var(--bookings)}
.feature.services{background:var(--services)}
.feature.events{background:var(--events)}
.feature svg{flex:none;margin-top:0}
.feature h3{font-size:17px;font-weight:700;margin-top:4px;letter-spacing:.3px}
.feature p{font-size:11.5px;line-height:23px;margin-top:4px;color:#f3e6e0}
.feature a{display:block;font-size:11.5px;font-weight:700;margin-top:3px}
/* content */
.content{left:100px;top:615px;width:1000px;height:1494px;background:var(--white)}
.sidebar{left:768px;top:615px;width:332px;height:1494px;background:var(--side)}
.section-title{font-size:16px;font-weight:700;color:#333;letter-spacing:.3px}
.rule{height:1px;background:var(--rule)}
.intro-photo{left:131px;top:714px;width:250px;height:174px;background:#eee;padding:7px;border:1px solid #e2e2e2}
.intro-photo div{width:100%;height:100%;background:linear-gradient(135deg,#d8d8d6,#8f8a86 55%,#3c3836)}
.intro-text{left:415px;top:716px;width:320px;font-size:11.5px;line-height:23px;color:#555}
.post{width:288px}
.post .photo{width:288px;height:169px}
.post h4{font-size:12.5px;font-weight:700;color:#222;line-height:23px;margin-top:17px}
.post p{font-size:11.5px;line-height:23px;color:#555;margin-top:6px}
.pager{left:348px;top:2030px;display:flex;gap:8px}
.pager span{height:23px;min-width:26px;padding:0 8px;border:1px solid #d6d6d6;background:#f5f5f5;font-size:11.5px;line-height:21px;text-align:center;color:#444}
.pager .wide{padding:0 12px;font-weight:600}
/* sidebar */
.links-list{left:801px;top:696px;list-style:none;font-size:11.5px;color:#555}
.links-list li{height:27.4px;line-height:27.4px;padding-left:12px;position:relative}
.links-list li::before{content:"›";position:absolute;left:0;color:#999}
.event{left:801px;width:280px;display:flex;gap:18px}
.event .thumb{width:97px;height:80px;flex:none;border:2px solid #fff}
.event h5{font-size:11px;font-weight:700;color:#222;line-height:21px;margin-top:4px}
.event em{font-size:11px;color:#999;display:block;margin-top:6px}
.about-photo{left:801px;top:1486px;width:272px;height:155px;background:linear-gradient(180deg,#c7ced6 0%,#8e9aa6 55%,#3b4047 100%)}
.about-title{left:801px;top:1652px;width:272px;font-size:12.5px;font-weight:700;color:#222;line-height:23px}
.about-text{left:801px;top:1704px;width:272px;font-size:11.5px;line-height:23px;color:#555}
.btn{left:803px;top:1790px;width:150px;height:40px;background:var(--red);color:#fff;font-size:12px;font-weight:700;text-align:center;line-height:40px;box-shadow:0 2px 0 #7a1a1f}
.calendar{left:801px;top:1862px;width:276px;height:211px;background:#fff;border:1px solid #ddd}
.cal-head{height:34px;display:flex;align-items:center;justify-content:space-between;border-bottom:1px solid #ddd}
.cal-head b{font-size:11px;font-weight:700;color:#333}
.cal-nav{width:18px;height:34px;background:var(--teal);display:flex;align-items:center;justify-content:center}
.cal-grid{margin:6px 16px;border-collapse:collapse;width:240px}
.cal-grid th{font-size:8.5px;font-weight:700;color:#333;height:22px}
.cal-grid td{border:1px solid #ddd;font-size:8.5px;text-align:center;height:26px;color:#444}
.cal-grid td.off{color:#ccc}
.cal-grid td.today{background:var(--today);color:#fff}
/* footer */
.site-footer{left:100px;top:2109px;width:1000px;height:343px;background:var(--footer)}
.foot-col{top:2145px}
.foot-col h6{font-size:13.5px;font-weight:700;color:#fff;letter-spacing:.3px;margin-bottom:12px}
.foot-col ul{list-style:none;font-size:11px;color:var(--footer-text)}
.foot-col li{height:24px;line-height:24px}
.social li{display:flex;align-items:center;gap:6px;height:37px}
.social i{width:26px;height:26px;border-radius:50%;background:#444;display:block}
.copyright{left:100px;top:2416px;width:1000px;text-align:center;font-size:11px;color:#777}
</style>
</head>
<body>
<div class="hero-scene abs" role="img" aria-label="Sunset over a rock arch standing in the sea"></div>

<header class="site-header abs">
  <div class="brand">
    <span class="brand-mark"></span>
    <div>
      <div class="brand-name">GLN Marlow Trent &amp; Associates</div>
      <div class="brand-tag">CHARTERED PROFESSIONAL ACCOUNTANTS</div>
    </div>
  </div>
  <nav class="main-nav"><span>Home</span><span>Profile</span><span>Client Services</span><span>Resources</span><span>Contact</span></nav>
</header>

<div class="slider-arrow abs"></div>
<div class="slider-dot abs"></div>
<p class="hero-sub abs">WELCOME AND THANK YOU FOR VISITING</p>
<h1 class="hero-title abs">THE GLN MARLOW TRENT &amp; ASSOCIATES</h1>

<section class="features abs">
  <div class="feature bookings">
    <svg width="48" height="104" viewBox="0 0 48 104" fill="none" stroke="#3a0f12" stroke-width="4"><path d="M24 0v18"/><rect x="3" y="18" width="42" height="84" rx="21" fill="#3a0f12"/><path d="M3 52h42M24 18v34" stroke="#8c2a30"/></svg>
    <div><h3>MY BOOKINGS</h3><p>Lorem Ipsum is simply dummy text<br>of the printing and typesetting...</p><a>Read More info ›</a></div>
  </div>
  <div class="feature services">
    <svg width="66" height="60" viewBox="0 0 66 60" fill="#3d1508"><circle cx="14" cy="14" r="9"/><circle cx="52" cy="14" r="9"/><circle cx="33" cy="22" r="11"/><path d="M0 48c0-12 6-20 14-20s12 6 12 10v10zM66 48c0-12-6-20-14-20s-12 6-12 10v10zM14 60c0-14 8-24 19-24s19 10 19 24z"/></svg>
    <div><h3>CLIENT SERVICES</h3><p>Lorem Ipsum is simply dummy text<br>of the printing and typesetting...</p><a>Read More info ›</a></div>
  </div>
  <div class="feature events">
    <svg width="64" height="62" viewBox="0 0 64 62" fill="none" stroke="#142d2c" stroke-width="5"><rect x="3" y="8" width="58" height="51" rx="4"/><path d="M3 22h58M16 2v12M48 2v12M18 30v24M32 30v24M46 30v24M8 38h48M8 48h48" stroke-width="3"/></svg>
    <div><h3>EVENTS CALENDAR</h3><p>Lorem Ipsum is simply dummy text<br>of the printing and typesetting...</p><a>Read More info ›</a></div>
  </div>
</section>

<main class="content abs"></main>
<aside class="sidebar abs"></aside>

<h2 class="section-title abs" style="left:130px;top:648px">WELCOME TO GLN MARLOW TRENT &amp; ASSOCIATES</h2>
<div class="rule abs" style="left:130px;top:687px;width:606px"></div>
<div class="intro-photo abs"><div role="img" aria-label="Person working with a calculator and documents at a desk"></div></div>
<p class="intro-text abs">Please note that, as of November 26, 2012, our Oakridge office has relocated to 14 Brenlow Court, Oakridge, NB E4K 2P7. Brenlow Court is located off Ferrin Drive, just past Halden's Flooring Depot on the Carrick Road on your way out of the city. addition to providing you with a profile of our firm and the services we provide, this Website has been designed to become a helpful resource tool to you...</p>

<h2 class="section-title abs" style="left:130px;top:924px">RECENT POSTS</h2>
<div class="rule abs" style="left:130px;top:963px;width:606px"></div>

<article class="post abs" style="left:129px;top:992px"><div class="photo" role="img" aria-label="Two colleagues working together at a laptop" style="background:linear-gradient(135deg,#eef0f2,#9fb3c8 55%,#3e5a86)"></div><h4>LOREM IPSUM IS SIMPLY DUMMY TEXT OF THE PRINTING</h4><p>Lorem Ipsum is simply dummy text of the printing and typesetting industry. Lorem Ipsum has been the industry's standard dummy text ever...</p></article>
<article class="post abs" style="left:448px;top:992px"><div class="photo" role="img" aria-label="Two businessmen in suits outside office towers" style="background:linear-gradient(135deg,#7fa6c8,#4a5e74 50%,#1f2227)"></div><h4>LOREM IPSUM IS SIMPLY DUMMY TEXT OF THE PRINTING</h4><p>Lorem Ipsum is simply dummy text of the printing and typesetting industry. Lorem Ipsum has been the industry's standard dummy text ever...</p></article>
<article class="post abs" style="left:129px;top:1334px"><div class="photo" role="img" aria-label="Hands reviewing a printed bar chart with a pen" style="background:linear-gradient(135deg,#a47a52,#d9cfc2 55%,#f2f2f2)"></div><h4>LOREM IPSUM IS SIMPLY DUMMY TEXT OF THE PRINTING</h4><p>Lorem Ipsum is simply dummy text of the printing and typesetting industry. Lorem Ipsum has been the industry's standard dummy text ever...</p></article>
<article class="post abs" style="left:448px;top:1334px"><div class="photo" role="img" aria-label="Black and white close-up of a wristwatch on a suited arm" style="background:linear-gradient(135deg,#e0e0e0,#8a8a8a 50%,#202020)"></div><h4>LOREM IPSUM IS SIMPLY DUMMY TEXT OF THE PRINTING</h4><p>Lorem Ipsum is simply dummy text of the printing and typesetting industry. Lorem Ipsum has been the industry's standard dummy text ever...</p></article>
<article class="post abs" style="left:129px;top:1679px"><div class="photo" role="img" aria-label="Smiling businessman giving a thumbs up" style="background:linear-gradient(135deg,#6f7f95,#c9a896 50%,#e8e8ea)"></div><h4>LOREM IPSUM IS SIMPLY DUMMY TEXT OF THE PRINTING</h4><p>Lorem Ipsum is simply dummy text of the printing and typesetting industry. Lorem Ipsum has been the industry's standard dummy text ever...</p></article>
<article class="post abs" style="left:448px;top:1679px"><div class="photo" role="img" aria-label="Business handshake" style="background:linear-gradient(135deg,#6b4a30,#c9a47a 50%,#f0e4d0)"></div><h4>LOREM IPSUM IS SIMPLY DUMMY TEXT OF THE PRINTING</h4><p>Lorem Ipsum is simply dummy text of the printing and typesetting industry. Lorem Ipsum has been the industry's standard dummy text ever...</p></article>

<nav class="pager abs"><span class="wide">Prev</span><span>1</span><span>2</span><span>3</span><span>4</span><span>5</span><span>6</span><span>...</span><span>22</span><span class="wide">Next</span></nav>

<h2 class="section-title abs" style="left:801px;top:646px">LINKS</h2>
<div class="rule abs" style="left:801px;top:679px;width:272px"></div>
<ul class="links-list abs"><li>Categories</li><li>Events Calendar</li><li>Financial Tools</li><li>Info Center</li><li>Locations</li><li>My Bookings</li><li>Sample Page</li><li>Tags</li><li>Links</li></ul>

<h2 class="section-title abs" style="left:801px;top:963px">LATEST EVENT</h2>
<div class="rule abs" style="left:801px;top:997px;width:272px"></div>
<div class="event abs" style="top:1015px"><div class="thumb" role="img" aria-label="Businesswoman with glasses" style="background:linear-gradient(135deg,#f0f0f0,#cdb8a0 60%,#6a6a6a)"></div><div><h5>LOREM IPSUM IS SIMPLY<br>DUMMY TEXT</h5><em>Posted on 27 March 2015</em></div></div>
<div class="event abs" style="top:1118px"><div class="thumb" role="img" aria-label="Two colleagues at a laptop" style="background:linear-gradient(135deg,#e6e8ea,#8fa4bc 60%,#3e5a86)"></div><div><h5>LOREM IPSUM IS SIMPLY<br>DUMMY TEXT</h5><em>Posted on 27 March 2015</em></div></div>
<div class="event abs" style="top:1221px"><div class="thumb" role="img" aria-label="Team meeting around a table" style="background:linear-gradient(135deg,#9a8c7a,#5d5048 60%,#2e2a28)"></div><div><h5>LOREM IPSUM IS SIMPLY<br>DUMMY TEXT</h5><em>Posted on 27 March 2015</em></div></div>
<div class="event abs" style="top:1324px"><div class="thumb" role="img" aria-label="Business partners smiling in an office" style="background:linear-gradient(135deg,#e8e8e8,#9aa6b2 60%,#2c2f36)"></div><div><h5>LOREM IPSUM IS SIMPLY<br>DUMMY TEXT</h5><em>Posted on 27 March 2015</em></div></div>

<h2 class="section-title abs" style="left:801px;top:1436px">ABOUT GLN</h2>
<div class="rule abs" style="left:801px;top:1469px;width:272px"></div>
<div class="about-photo abs" role="img" aria-label="Glass office towers under a clear sky"></div>
<h4 class="about-title abs">LOREM IPSUM IS SIMPLY DUMMY TEXT OF THE PRINTING</h4>
<p class="about-text abs">Lorem Ipsum is simply dummy text of the printing and typesetting industry. Lorem Ipsum has been the industry's standard dummy text ever...</p>
<div class="btn abs">READ MORE INFO</div>

<div class="calendar abs">
  <div class="cal-head">
    <span class="cal-nav"><svg width="8" height="12" viewBox="0 0 8 12"><path d="M6 1L2 6l4 5" stroke="#fff" stroke-width="2" fill="none"/></svg></span>
    <b>APRIL 2015</b>
    <span class="cal-nav"><svg width="8" height="12" viewBox="0 0 8 12"><path d="M2 1l4 5-4 5" stroke="#fff" stroke-width="2" fill="none"/></svg></span>
  </div>
  <table class="cal-grid">
    <tr><th>Mon</th><th>Tue</th><th>Wed</th><th>Thu</th><th>Fri</th><th>Sat</th><th>Sun</th></tr>
    <tr><td>1</td><td>2</td><td>3</td><td>4</td><td>5</td><td>6</td><td>7</td></tr>
    <tr><td>8</td><td>9</td><td>10</td><td>11</td><td>12</td><td>13</td><td>14</td></tr>
    <tr><td>15</td><td>16</td><td>17</td><td>18</td><td>19</td><td>20</td><td>21</td></tr>
    <tr><td>22</td><td>23</td><td>24</td><td>25</td><td>26</td><td>27</td><td>28</td></tr>
    <tr><td>29</td><td class="today">30</td><td>31</td><td class="off">1</td><td class="off">2</td><td class="off">3</td><td class="off">4</td></tr>
  </table>
</div>

<footer class="site-footer abs"></footer>
<div class="foot-col abs" style="left:139px"><h6>INTERESTING LINKS</h6><ul><li>Here are some interesting links for you!</li><li>Here are some interesting links</li><li>Here are some interesting links for</li><li>Here are some interesting</li><li>Here are some interesting links for you!</li><li>Here are some interesting</li><li>Here are some interesting links for you!</li><li>Here are some interesting links</li></ul></div>
<div class="foot-col abs" style="left:438px"><h6>WELCOME</h6><ul><li>Categories</li><li>Client Services</li><li>Contact</li><li>Events Calendar</li><li>Financial Tools</li><li>Home</li><li>Info Center</li><li>Locations</li></ul></div>
<div class="foot-col abs" style="left:575px;padding-top:30px"><ul><li>My Bookings</li><li>Profile</li><li>Resources</li><li>Sample Page</li><li>Tags</li><li>Links</li></ul></div>
<div class="foot-col abs" style="left:737px"><h6>INFORMATION</h6><ul><li>Terms &amp; Condition</li><li>Privacy policy</li><li>Disclaimer</li></ul></div>
<div class="foot-col abs" style="left:919px"><h6>FOLLOW US</h6><ul class="social"><li><i></i>: Friendfold</li><li><i></i>: Circlecast</li><li><i></i>: Vidstream</li><li><i></i>: Chirpline</li></ul></div>
<p class="copyright abs">© Copyright - GLN Marlow Trent - All rights reserved.</p>
</body>
</html>
```